Lowell Brandt

20 Year Licensed Master Barber specializing in:
men/women cuts, Grooming, Straight razor Shaving and tape line enhancement, beard grooming, eye brow enhancement, South of France, Hot Towel Treatments, Scalp, Blow outs, Shags, Custom Design,RazorCuts,Shear Cuts, Bobs, Perms, Relaxers, Shoe Shine.
Please create a wonderful business card incorporating all the info above and selecting one of the photos. Please be creative.

Barber

```html
<!DOCTYPE html>
<html lang="en">
<head>
<meta charset="utf-8">
<title>Lowell Brandt – Barber Business Card</title>
<link href="https://fonts.googleapis.com/css2?family=Lato:wght@400;700&display=swap" rel="stylesheet">
<style>
  :root {
    --page: #d6d6d6;
    --card-dark: #141414;
    --card-dark-2: #1d1d1d;
    --band: #ffffff;
    --ink-light: #f2f2f2;
    --ink-muted: #c9c9c9;
    --mark-navy: #2b3080;
    --photo-hi: #3b3b3b;
    --photo-lo: #161616;
  }
  * { box-sizing: border-box; margin: 0; padding: 0; }
  html, body { width: 1200px; height: 1200px; overflow: hidden; }
  body {
    background: var(--page);
    font-family: 'Lato', sans-serif;
    position: relative;
  }
  .card {
    position: absolute;
    left: 221px;
    width: 772px;
    height: 440px;
    overflow: hidden;
    background: linear-gradient(180deg, var(--card-dark-2), var(--card-dark));
  }
  .card--front { top: 105px; }
  .card--back  { top: 624px; }

  /* front */
  .front__portrait {
    position: absolute;
    left: 250px; top: 0;
    width: 290px; height: 440px;
    background: radial-gradient(ellipse at 50% 30%, var(--photo-hi) 0%, #262626 45%, var(--photo-lo) 80%);
    opacity: .9;
  }
  .front__tagline {
    position: absolute;
    left: 195px; top: 38px;
    width: 90px;
    color: #8a8a8a;
    font-size: 15px;
    line-height: 15px;
    font-weight: 700;
    letter-spacing: 1px;
    text-transform: uppercase;
    text-align: center;
  }
  .front__band {
    position: absolute;
    left: 0; top: 239px;
    width: 100%; height: 122px;
    background: var(--band);
    display: flex; align-items: center; justify-content: center;
  }

  .brand-mark {
    width: 106px; height: 106px;
    border-radius: 50%;
    border: 3px solid var(--mark-navy);
    display: flex; align-items: center; justify-content: center;
    text-align: center;
    color: var(--mark-navy);
    font-weight: 700;
    font-size: 15px;
    line-height: 17px;
    text-transform: uppercase;
  }
  .brand-mark--large {
    width: 144px; height: 144px;
    font-size: 21px; line-height: 24px;
  }

  /* back */
  .back__panel {
    position: absolute;
    left: 0; top: 0;
    width: 252px; height: 100%;
    background: var(--band);
    display: flex; justify-content: center;
    padding-top: 36px;
  }
  .back__portrait {
    position: absolute;
    left: 480px; top: 0;
    width: 240px; height: 440px;
    background: radial-gradient(ellipse at 45% 35%, #2e2e2e 0%, #1f1f1f 45%, var(--photo-lo) 80%);
  }
  .back__seal {
    position: absolute;
    left: 686px; top: 42px;
    width: 66px; height: 66px;
    border-radius: 50%;
    border: 2px solid #3a3a3a;
    color: #444;
    font-size: 10px; line-height: 12px;
    font-weight: 700;
    text-transform: uppercase;
    display: flex; align-items: center; justify-content: center;
    text-align: center;
  }
  .back__identity {
    position: absolute;
    right: 30px; top: 156px;
    text-align: right;
    color: var(--ink-light);
  }
  .back__name { font-size: 32px; font-weight: 700; letter-spacing: .5px; }
  .back__role { font-size: 19px; color: var(--ink-muted); margin-top: 2px; }

  .contact-list {
    position: absolute;
    left: 294px; top: 238px;
    list-style: none;
    color: var(--ink-light);
    font-size: 17px;
  }
  .contact-list li {
    display: flex; align-items: center;
    height: 39.5px;
  }
  .contact-list svg { width: 16px; height: 16px; margin-right: 12px; flex: none; }
</style>
</head>
<body>

<section class="card card--front">
  <div class="front__portrait" role="img" aria-label="Portrait photo of the barber in a black tuxedo and bow tie"></div>
  <p class="front__tagline">The Steady Hand Lowell</p>
  <div class="front__band">
    <div class="brand-mark">Lowell<br>Brandt</div>
  </div>
</section>

<section class="card card--back">
  <div class="back__portrait" role="img" aria-label="Faded portrait photo of the barber in a suit"></div>
  <div class="back__seal">Lowell<br>Brandt</div>

  <div class="back__panel">
    <div class="brand-mark brand-mark--large">Lowell<br>Brandt</div>
  </div>

  <div class="back__identity">
    <p class="back__name">YOUR NAME</p>
    <p class="back__role">CEO</p>
  </div>

  <ul class="contact-list">
    <li>
      <svg viewBox="0 0 16 16"><rect x="4" y="1" width="8" height="14" rx="1.5" fill="none" stroke="#f2f2f2" stroke-width="1.6"/><circle cx="8" cy="12.3" r=".9" fill="#f2f2f2"/></svg>
      0000 1234 456789
    </li>
    <li>
      <svg viewBox="0 0 16 16"><rect x="1" y="3" width="14" height="10" rx="1" fill="#f2f2f2"/><path d="M1.5 3.5 8 9l6.5-5.5" fill="none" stroke="#141414" stroke-width="1.3"/></svg>
      email@companyname.com
    </li>
    <li>
      <svg viewBox="0 0 16 16"><path d="M8 1.5a4.5 4.5 0 0 0-4.5 4.5c0 3.4 4.5 8.5 4.5 8.5s4.5-5.1 4.5-8.5A4.5 4.5 0 0 0 8 1.5z" fill="#f2f2f2"/><circle cx="8" cy="6" r="1.6" fill="#141414"/></svg>
      address, city, Country.
    </li>
    <li>
      <svg viewBox="0 0 16 16" fill="none" stroke="#f2f2f2" stroke-width="1.2"><circle cx="8" cy="8" r="6.5"/><ellipse cx="8" cy="8" rx="3" ry="6.5"/><path d="M1.5 8h13M2.5 4.8h11M2.5 11.2h11"/></svg>
      companyname.com
    </li>
  </ul>
</section>

</body>
</html>
```